Fashion Design Business Card

I need a new business card designed for a new fashion company. I have attached what I have currently designed. I want it more feminine looking, the logo needs to be gold. I want it simple, feminine and stylish. Please give me some different ideas with the fonts.

I need to send the design we currently have, as we have worked out the logo.
You also need all of our details
Fashion

```html
<!DOCTYPE html>
<html lang="en">
<head>
<meta charset="utf-8">
<title>Marina Ellwood – Business Card</title>
<link rel="stylesheet" href="https://fonts.googleapis.com/css2?family=Open+Sans:wght@300;400;600&display=swap">
<style>
  :root {
    --page-bg: #ffffff;
    --card-plum: #5f1046;
    --card-plum-light: #6a1550;
    --text-white: #ffffff;
    --accent-gold: #f0a81c;
    --brand-gold: #e9b52a;
  }
  * { margin: 0; padding: 0; box-sizing: border-box; }
  html, body {
    width: 1200px;
    height: 900px;
    overflow: hidden;
    background: var(--page-bg);
    font-family: "Open Sans", sans-serif;
  }
  .canvas {
    position: relative;
    width: 1200px;
    height: 900px;
  }
  .business-card {
    position: absolute;
    left: 80px;
    top: 124px;
    width: 1090px;
    height: 620px;
    border-radius: 60px;
    background: radial-gradient(circle at 25% 50%, var(--card-plum-light) 0%, var(--card-plum) 60%);
    border: 2px solid #3d0a2c;
    overflow: hidden;
  }
  .brand-mark {
    position: absolute;
    left: 60px;
    top: 260px;
    display: flex;
    align-items: center;
    gap: 18px;
    font-family: "Open Sans", sans-serif;
    font-weight: 600;
    font-size: 40px;
    color: var(--brand-gold);
    white-space: nowrap;
  }
  .brand-dot {
    width: 34px;
    height: 34px;
    border-radius: 50%;
    background: var(--brand-gold);
    flex: none;
  }
  .identity {
    position: absolute;
    right: 108px;
    top: 92px;
    text-align: right;
  }
  .identity-name {
    font-weight: 400;
    font-size: 56px;
    line-height: 1.1;
    color: var(--text-white);
  }
  .identity-role {
    font-weight: 400;
    font-size: 34px;
    letter-spacing: 3px;
    line-height: 1.1;
    color: var(--accent-gold);
    margin-top: 2px;
  }
  .contact-list {
    position: absolute;
    right: 108px;
    top: 472px;
    list-style: none;
    text-align: right;
    color: var(--text-white);
    font-weight: 400;
    font-size: 26px;
    line-height: 40px;
  }
  .contact-label { margin-right: 10px; }
</style>
</head>
<body>
  <main class="canvas">
    <section class="business-card" aria-label="Business card">
      <div class="brand-mark">
        <span class="brand-dot" aria-hidden="true"></span>
        <span class="brand-name">Marina Ellwood</span>
      </div>

      <header class="identity">
        <h1 class="identity-name">Marina Ellwood</h1>
        <p class="identity-role">fashion designer</p>
      </header>

      <ul class="contact-list">
        <li class="contact-phone"><span class="contact-label">ph.</span>0400512736</li>
        <li class="contact-email"><span class="contact-label">email:</span>marina@marinaellwood.com</li>
        <li class="contact-web"><span class="contact-label">web:</span>www.marinaellwood.com</li>
      </ul>
    </section>
  </main>
</body>
</html>
```